Income Tax and Accounting Brochure

I need a brochure using my new logo (file attached). I do tax work and accounting work. I am an EA (QDX Enrolled Agent - logo attached) and would like this incorporated into the brochure. I also have a MSA in Accounting. Please incorporate the text that I have provided in the brochure.

Target Market(s)

Tax Clients - both business and individuals

Industry/Entity Type

Accounting

Colors
0054AA
0677BA
7BADD7
CADEEF
E8F1F8

Requirements
Must have
• Use my logo and the QDX EA file in the brochure
Nice to have
• I would like to see a brochure that I can customize with my own text if possible.

```html
<!DOCTYPE html>
<html lang="en">
<head>
<meta charset="utf-8">
<title>Northvale Accounting &amp; Consulting – Tax Brochure</title>
<link href="https://fonts.googleapis.com/css2?family=Rubik:ital,wght@0,400;0,500;0,600;1,400&display=swap" rel="stylesheet">
<style>
  :root {
    --blue-deep: #0054AA;
    --blue-mid: #0677BA;
    --blue-light: #7BADD7;
    --blue-pale: #CADEEF;
    --blue-mist: #E8F1F8;
    --navy-bar: #1d2231;
    --red: #c8102e;
    --ink: #2a2d34;
    --backdrop: #a6a8ac;
    --white: #ffffff;
  }
  * { box-sizing: border-box; margin: 0; padding: 0; }
  html, body { width: 1200px; height: 851px; overflow: hidden; }
  body {
    background: var(--backdrop);
    font-family: "Rubik", Arial, sans-serif;
    color: var(--ink);
    position: relative;
  }
  .page {
    position: absolute;
    top: 45px;
    width: 537px;
    height: 760px;
    background: var(--white);
    overflow: hidden;
  }
  .page--front { left: 43px; }
  .page--back { left: 620px; }
  .abs { position: absolute; }
  .page-art { position: absolute; left: 0; top: 0; width: 537px; height: 760px; }

  /* brand */
  .brand { display: flex; align-items: center; gap: 7px; }
  .brand-dot { width: 46px; height: 46px; border-radius: 50%; flex: none; }
  .brand-name {
    font-weight: 500;
    font-size: 14px;
    line-height: 17px;
    letter-spacing: 0.8px;
    text-transform: uppercase;
  }
  .brand--front { left: 288px; top: 86px; }
  .brand--front .brand-dot { background: var(--blue-deep); }
  .brand--front .brand-name { color: var(--blue-deep); }
  .brand--back { left: 258px; top: 603px; }
  .brand--back .brand-dot { background: var(--white); width: 56px; height: 56px; }
  .brand--back .brand-name { color: var(--white); font-size: 15px; line-height: 19px; }

  /* section bars */
  .section-bar {
    position: absolute;
    left: 49px;
    width: 440px;
    height: 25px;
    background: var(--navy-bar);
    color: var(--white);
    font-weight: 500;
    font-size: 14.5px;
    line-height: 25px;
    padding-left: 34px;
  }
  .section-bar::before {
    content: "";
    position: absolute;
    left: -1px; top: -1px;
    width: 27px; height: 27px;
    border-radius: 50%;
    background: var(--white);
    border: 4px solid var(--blue-deep);
  }

  .body-copy {
    font-size: 10px;
    line-height: 13.6px;
    text-align: justify;
  }

  /* front */
  .headshot {
    left: 49px; top: 475px; width: 113px; height: 165px;
    background: linear-gradient(160deg, #3a3c42, #1b1c20 60%, #5c5f66);
  }
  .principal { left: 174px; top: 469px; width: 316px; }
  .principal-name {
    font-size: 15px; font-weight: 500; color: var(--blue-deep);
    margin-bottom: 3px;
  }
  .principal-name em { color: var(--red); font-weight: 400; }
  .principal .body-copy + .body-copy { margin-top: 13.6px; }

  .contact { text-align: right; color: var(--white); font-weight: 600; }
  .contact-line { display: flex; align-items: center; justify-content: flex-end; gap: 6px; }
  .contact--front { right: 48px; top: 694px; }
  .contact--front .phone { font-size: 22px; line-height: 26px; }
  .contact--front .web { font-size: 14px; line-height: 18px; }
  .contact--back { right: 49px; top: 686px; }
  .contact--back .phone { font-size: 25px; line-height: 29px; }
  .contact--back .web { font-size: 16px; line-height: 20px; }

  /* back */
  .copy-block { left: 49px; width: 439px; }
  .lead { font-size: 10.4px; font-weight: 500; margin-bottom: 2px; }
  .copy-block .body-copy + .body-copy { margin-top: 13.6px; }

  .benefits { left: 49px; top: 276px; width: 439px; list-style: none; }
  .benefits::before {
    content: ""; position: absolute; left: 5px; top: 6px; bottom: 6px;
    width: 1px; background: var(--blue-light);
  }
  .benefits li { position: relative; padding-left: 17px; margin-bottom: 13.6px; }
  .benefits li svg { position: absolute; left: 0; top: 1px; }

  .address {
    left: 40px; top: 702px; color: var(--white);
    font-size: 10.5px; line-height: 13.6px;
  }
  .address strong { font-weight: 600; }
</style>
</head>
<body>

<!-- Front page -->
<section class="page page--front">
  <svg class="page-art" viewBox="0 0 537 760" aria-hidden="true">
    <defs>
      <linearGradient id="bandFront" x1="0" y1="0" x2="1" y2="0">
        <stop offset="0" stop-color="#0054AA"/>
        <stop offset="1" stop-color="#0a4fa3"/>
      </linearGradient>
    </defs>
    <path d="M0 430 Q 250 300 537 380 L537 760 L0 760 Z" fill="#ffffff"/>
    <path d="M70 402 Q 300 300 537 388 L537 373 Q 300 285 70 402 Z" fill="#0054AA"/>
    <path d="M30 760 Q 240 650 360 640 Q 210 670 65 760 Z" fill="#c8102e"/>
    <path d="M70 760 Q 280 660 537 688 L537 760 Z" fill="url(#bandFront)"/>
  </svg>
  <div class="abs" role="img" aria-label="Photo of a delighted woman in an orange blouse celebrating at her laptop"
       style="left:0;top:0;width:537px;height:430px;clip-path:path('M0 0 H537 V380 Q 250 300 0 430 Z');background:linear-gradient(120deg,#d9d6d2 0%,#efe9e3 35%,#e8744a 55%,#f1ede9 80%,#dcdfe3 100%);"></div>

  <div class="abs brand brand--front">
    <span class="brand-dot"></span>
    <span class="brand-name">Northvale Accounting<br>&amp; Consulting, LLC</span>
  </div>

  <h2 class="section-bar" style="top:437px;">About</h2>

  <div class="abs headshot" role="img" aria-label="Portrait photo of the principal"></div>

  <div class="abs principal">
    <h3 class="principal-name">Marian R Holloway, MSA EA <em>(Principal)</em></h3>
    <p class="body-copy">I have a Masters' Degree in accounting and am an QDX Enrolled Agent. I am also a LedgerLeaf Advanced Certified Consultant in both the online and desktop products including Enterprise and Point of Sale. I provide individual and small business tax services, Accounting, bookkeeping, QDX representation, insurance audit representation, business license assistance and more.</p>
    <p class="body-copy">I have experience working with a wide variety of clients from the point where they first decide they want to start a business. They are often unsure about what to do first- I have a lot of experience to offer you.</p>
  </div>

  <div class="abs contact contact--front">
    <div class="contact-line phone">
      <svg width="16" height="16" viewBox="0 0 24 24" aria-hidden="true"><path fill="#fff" d="M6.6 10.8a15.1 15.1 0 0 0 6.6 6.6l2.2-2.2c.3-.3.7-.4 1-.2 1.1.4 2.3.6 3.6.6.6 0 1 .4 1 1V20c0 .6-.4 1-1 1A17 17 0 0 1 3 4c0-.6.4-1 1-1h3.5c.6 0 1 .4 1 1 0 1.3.2 2.5.6 3.6.1.3 0 .7-.2 1z"/></svg>
      (555)010-4872
    </div>
    <div class="contact-line web">
      <svg width="14" height="14" viewBox="0 0 24 24" aria-hidden="true"><g fill="none" stroke="#fff" stroke-width="1.8"><circle cx="12" cy="12" r="10"/><path d="M2 12h20M12 2c3 3 3 17 0 20M12 2c-3 3-3 17 0 20"/></g></svg>
      NORTHVALEACCT.COM
    </div>
  </div>
</section>

<!-- Back page -->
<section class="page page--back">
  <svg class="page-art" viewBox="0 0 537 760" aria-hidden="true">
    <defs>
      <linearGradient id="bandBack" x1="0" y1="1" x2="1" y2="0">
        <stop offset="0" stop-color="#0054AA"/>
        <stop offset="1" stop-color="#0677BA"/>
      </linearGradient>
    </defs>
    <path d="M0 687 Q 200 550 356 563 Q 190 570 0 672 Z" fill="#c8102e"/>
    <path d="M0 698 Q 230 560 537 568 L537 760 L0 760 Z" fill="url(#bandBack)"/>
  </svg>

  <h2 class="section-bar" style="top:46px;">What a joy it is to watch success in action!</h2>

  <div class="abs copy-block" style="top:84px;">
    <h3 class="lead">Tax Preparation – why hire us?</h3>
    <p class="body-copy">Preparing your own income tax return can be a task that leaves you with more questions than answers. According to a study released by the National Audit Bureau last year, most taxpayers (77% of 71 million taxpayers) believe they benefited from using a professional tax preparer.</p>
    <p class="body-copy">Whether we like it or not, today's tax laws are so complicated that filing a relatively simple return can be confusing. It is just too easy to overlook deductions and credits to which you are entitled. Even if you use a computer software program there's no substitute for the assistance of an experienced tax professional.</p>
  </div>

  <h2 class="section-bar" style="top:232px;">Here's what your get...</h2>

  <ul class="abs benefits body-copy">
    <li><svg width="11" height="11" viewBox="0 0 12 12" aria-hidden="true"><circle cx="6" cy="6" r="6" fill="#c8102e"/><path d="M3.2 6.2l1.9 1.8 3.7-3.8" fill="none" stroke="#fff" stroke-width="1.6"/></svg>Your tax return will be checked and rechecked by our computer software identifying potential problems the QDX may look at more closely and reviewing the math to limit QDX contacts.</li>
    <li><svg width="11" height="11" viewBox="0 0 12 12" aria-hidden="true"><circle cx="6" cy="6" r="6" fill="#c8102e"/><path d="M3.2 6.2l1.9 1.8 3.7-3.8" fill="none" stroke="#fff" stroke-width="1.6"/></svg>Your tax return can be filed electronically so you will get a refund back quicker.</li>
    <li><svg width="11" height="11" viewBox="0 0 12 12" aria-hidden="true"><circle cx="6" cy="6" r="6" fill="#c8102e"/><path d="M3.2 6.2l1.9 1.8 3.7-3.8" fill="none" stroke="#fff" stroke-width="1.6"/></svg>Our staff will show you how to adjust your payroll withholding to get more money back each week. Why give the QDX an interest free loan for up to 16 months.</li>
    <li><svg width="11" height="11" viewBox="0 0 12 12" aria-hidden="true"><circle cx="6" cy="6" r="6" fill="#c8102e"/><path d="M3.2 6.2l1.9 1.8 3.7-3.8" fill="none" stroke="#fff" stroke-width="1.6"/></svg>We will show you potential deductions to limit your tax liability for next year. In addition, we will give you a sheet of commonly overlooked deductions to limit the following year's tax liability.</li>
  </ul>

  <h2 class="section-bar" style="top:448px;">Books a Mess: No Problem!</h2>

  <div class="abs copy-block" style="top:492px;">
    <p class="body-copy">If you own a small business and haven't kept up your bookkeeping, don't worry. We can help you. We'll prepare your bookkeeping for the year, prepare a full Schedule C, as well as your personal income tax return. Then we'll help you set up an easy system that allows you to keep your books in tip-top shape next year.</p>
  </div>

  <div class="abs brand brand--back">
    <span class="brand-dot"></span>
    <span class="brand-name">Northvale Accounting<br>&amp; Consulting, LLC</span>
  </div>

  <address class="abs address" style="font-style:normal;">
    <strong>Northvale Accounting &amp; Consulting, LLC</strong><br>
    2280 Harrow Mill Rd, PO Box 14<br>
    Fernbrook, VA 20000
  </address>

  <div class="abs contact contact--back">
    <div class="contact-line phone">
      <svg width="18" height="18" viewBox="0 0 24 24" aria-hidden="true"><path fill="#fff" d="M6.6 10.8a15.1 15.1 0 0 0 6.6 6.6l2.2-2.2c.3-.3.7-.4 1-.2 1.1.4 2.3.6 3.6.6.6 0 1 .4 1 1V20c0 .6-.4 1-1 1A17 17 0 0 1 3 4c0-.6.4-1 1-1h3.5c.6 0 1 .4 1 1 0 1.3.2 2.5.6 3.6.1.3 0 .7-.2 1z"/></svg>
      (555)010-4872
    </div>
    <div class="contact-line web">
      <svg width="16" height="16" viewBox="0 0 24 24" aria-hidden="true"><g fill="none" stroke="#fff" stroke-width="1.8"><circle cx="12" cy="12" r="10"/><path d="M2 12h20M12 2c3 3 3 17 0 20M12 2c-3 3-3 17 0 20"/></g></svg>
      NORTHVALEACCT.COM
    </div>
  </div>
</section>

</body>
</html>
```